Velmor Hub Redesign

velmorhub.com is one of our old, high-traffic multilingual site.

its interface is very old, so we want to redesign it to give a modern, attractive design, with comfortable colors and layout.

beside the current content of the main page we want to add two places for dynamic banners.

The site has an App in Orbit OS and Droplet, we want an ad in a noticeable place for it.

this ad will be permanent.

the site now has 12 languages, but we may add new languages soon, so design must consider this.

redesign of two internal pages also required:
- the main listing page, example: http://www.velmorhub.info/en/cat/252
- the article view page: http://www.velmorhub.info/en/10323

Reason: want to receive more designs ...

```html
<!DOCTYPE html>
<html lang="en">
<head>
<meta charset="utf-8">
<title>Velmor Hub – Questions &amp; Answer</title>
<link href="https://fonts.googleapis.com/css2?family=Arimo:wght@400;700&family=Questrial&family=Ubuntu:wght@500;700&display=swap" rel="stylesheet">
<style>
:root{
  --green:#2e8b2e;
  --green-dark:#1d6b2a;
  --green-frame:#1f4d2f;
  --ink:#222;
  --text:#333;
  --muted:#888;
  --line:#dcdcdc;
  --bar:#f4f4f4;
  --btn:#2b2b2b;
  --foot:#4a4a4a;
  --foot-deep:#333;
}
*{box-sizing:border-box;margin:0;padding:0}
html,body{width:1002px;height:1200px;overflow:hidden;background:#fff}
body{position:relative;font-family:Arimo,Arial,sans-serif;color:var(--text)}
.abs{position:absolute}
a{color:inherit;text-decoration:none}

/* header */
.brand-mark{left:134px;top:18px;width:64px;height:64px;background:var(--ink)}
.brand-name{left:246px;top:26px;font-family:Ubuntu,sans-serif;font-weight:700;font-size:36px;color:var(--green);letter-spacing:-.5px;line-height:1}
.brand-tag{left:246px;top:70px;font-family:Questrial,sans-serif;font-size:14px;letter-spacing:2px;color:var(--green-dark)}
.app-ad{left:439px;top:28px;width:167px;height:62px;background:#efefef;border-radius:3px;display:flex;align-items:center;justify-content:space-around;font-family:Ubuntu,sans-serif;font-weight:500;font-size:15px}
.app-ad .os1{color:#555}
.app-ad .os2{color:#8bbb2a}
.book{left:630px;top:16px;width:94px;height:80px;border-radius:4px;background:linear-gradient(135deg,#c9b15a,#7a5a2a)}
.scholar{left:734px;top:40px;font-size:12.5px;line-height:16px;color:var(--green-dark)}
.scholar b{display:block;font-size:13px;color:var(--green)}

/* nav */
.nav{left:0;top:110px;width:1002px;height:26px;background:var(--green-dark)}
.nav ul{position:absolute;left:134px;top:0;display:flex;list-style:none;height:26px}
.nav li{font-family:Questrial,sans-serif;font-size:11px;color:#fff;line-height:26px;padding:0 19px;border-right:1px solid rgba(255,255,255,.15)}
.nav li.active{background:var(--green);padding:0 20px}

/* toolbar */
.toolbar{left:0;top:136px;width:1002px;height:38px;background:var(--bar);border-bottom:1px solid var(--line)}
.lang-label{left:134px;top:148px;font-family:Questrial,sans-serif;font-weight:700;font-size:12.5px;color:var(--ink)}
.lang-select{left:204px;top:145px;width:139px;height:20px;background:#fff;border:1px solid #ccc;font-size:9.5px;color:#777;padding:4px 7px}
.lang-select i{position:absolute;right:2px;top:2px;width:13px;height:14px;border:1px solid #aaa;background:#eee}
.lang-select i:after{content:"";position:absolute;left:3px;top:5px;border:3px solid transparent;border-top:4px solid #444}
.search-box{left:394px;top:145px;width:219px;height:20px;background:#fff;border:1px solid #ccc}
.search-btn{left:613px;top:145px;width:46px;height:20px;background:var(--btn);color:#fff;font-family:Questrial,sans-serif;font-size:10.5px;text-align:center;line-height:20px}
.adv{left:667px;top:149px;font-family:Questrial,sans-serif;font-size:10px;text-decoration:underline;color:var(--ink)}
.soc{width:20px;height:20px}

/* banners */
.banners{left:134px;top:192px;width:733px;height:254px;background:var(--green-frame)}
.slide{top:200px;width:353px;height:238px}
.slide .cap{position:absolute;left:0;bottom:0;width:100%;height:25px;background:rgba(0,0,0,.45);color:#fff;font-family:Ubuntu,sans-serif;font-weight:500;font-size:15px;text-align:center;line-height:25px}
.slide-a{left:143px;background:linear-gradient(180deg,#b9c9c9 0%,#d6caa0 40%,#9a8a5a 75%,#6e6245 100%)}
.slide-b{left:506px;background:linear-gradient(135deg,#f7c25a 0%,#f08a1e 40%,#8a3a08 70%,#1a0a02 100%)}

/* content box */
.panel{left:134px;top:466px;width:733px;height:578px;border:1px solid var(--line)}
.vsplit{left:611px;top:466px;width:1px;height:377px;background:var(--line)}
.hsplit{left:134px;top:498px;width:733px;height:1px;background:var(--line)}
.h-fatwa{left:148px;top:472px;font-family:Ubuntu,sans-serif;font-weight:500;font-size:19px;color:var(--green)}
.tab-on{background:var(--green);color:#fff}
.rtab{top:467px;height:31px;font-family:Questrial,sans-serif;font-size:10.5px;line-height:31px;text-align:center}
.fatwas{left:148px;top:510px;width:400px;list-style:none;font-size:9.8px;line-height:12px;color:var(--text)}
.fatwas li{position:relative;padding-left:12px;margin-bottom:13.6px}
.fatwas li:before{content:"»";position:absolute;left:0;top:0}
.checks{list-style:none;font-size:9.8px;color:var(--text)}
.checks li{position:relative;padding-left:18px}
.checks li:before{content:"";position:absolute;left:2px;top:0;width:4px;height:7px;border:solid #999;border-width:0 2px 2px 0;transform:rotate(40deg)}
.cats{left:624px;top:511px}
.cats li{height:26.4px}
.btn{height:25px;background:var(--btn);color:#fff;font-weight:700;font-size:10px;line-height:25px;padding:0 9px;display:flex;align-items:center;gap:9px}
.btn svg{width:7px;height:10px}

.tabs{left:134px;top:843px;width:733px;height:38px;border-top:1px solid var(--line);border-bottom:1px solid var(--line);display:flex}
.tabs div{font-family:Questrial,sans-serif;font-size:10.5px;line-height:12px;color:var(--green-dark);text-align:center;display:flex;align-items:center;justify-content:center;border-right:1px solid var(--line)}
.tabs div:last-child{border-right:0}
.tabs .tab-on{color:#fff}
.counsel{left:148px;top:900px;width:680px}
.counsel li{line-height:12px;margin-bottom:10.5px}

/* footer */
.footer{left:0;top:1062px;width:1002px;height:113px;background:var(--foot)}
.fcol{top:1074px;color:#fff;font-size:9.6px}
.fcol h4{font-size:10px;font-weight:700;margin-bottom:17px}
.fcol p{line-height:13.2px}
.fsep{top:1076px;width:1px;height:82px;background:#5f5f5f}
.fbig{font-family:Arimo,sans-serif;font-weight:700;font-size:13px;color:#fff}
.email{left:708px;top:1102px;width:159px;height:21px;background:#fff;border:1px solid #2a5db0;font-size:8.5px;color:#999;padding:5px 7px}
.signup{left:708px;top:1129px;width:54px;height:20px;background:#1d5fb3;color:#fff;font-weight:700;font-size:10.5px;text-align:center;line-height:20px}
.copy{left:0;top:1175px;width:1002px;height:25px;background:var(--foot-deep);color:#ddd;font-size:9.8px;text-align:center;line-height:25px}
</style>
</head>
<body>

<header>
  <div class="abs brand-mark"></div>
  <div class="abs brand-name">Velmor Hub</div>
  <div class="abs brand-tag">Questions &amp; Answer</div>
  <div class="abs app-ad"><span class="os1">Orbit OS</span><span class="os2">Droplet</span></div>
  <div class="abs book" role="img" aria-label="Decorated holy book resting on a wooden stand"></div>
  <div class="abs scholar">SHAYKH DAWUD`S<b>AL - FAROOQI</b></div>
</header>

<nav class="abs nav">
  <ul>
    <li class="active">Home</li><li>Catagories</li><li>New Fatwas</li><li>About Us</li><li>Article &amp; Books</li><li>Send a Questions</li><li style="border-right:0">Introduction of Islam</li>
  </ul>
</nav>

<div class="abs toolbar"></div>
<div class="abs lang-label">Language</div>
<div class="abs lang-select">English<i></i></div>
<div class="abs search-box"></div>
<div class="abs search-btn">Search</div>
<div class="abs adv">Advance Search</div>
<div class="abs soc" style="left:789px;top:145px;background:#3b5a9a"></div>
<div class="abs soc" style="left:818px;top:145px;background:#1da1e2"></div>
<div class="abs soc" style="left:847px;top:145px;background:#f39a1e"></div>

<section class="abs banners"></section>
<div class="abs slide slide-a" role="img" aria-label="Great mosque courtyard with minarets and a crowd of pilgrims"><div class="cap">Secrets of Islum</div></div>
<div class="abs slide slide-b" role="img" aria-label="Silhouette in prayer against an orange sunset sky"><div class="cap">Memorization of Quran</div></div>

<main>
  <div class="abs panel"></div>
  <div class="abs hsplit"></div>
  <div class="abs vsplit"></div>
  <h2 class="abs h-fatwa">New Fatwas</h2>
  <div class="abs rtab tab-on" style="left:612px;width:83px">Catagories</div>
  <div class="abs rtab" style="left:695px;width:48px;color:var(--green-dark)">Files</div>

  <ul class="abs fatwas">
    <li>Ruling on working with companies that do surveys on the Internet.</li>
    <li>Ruling on singling out ‘Ashoora for fasting.</li>
    <li>He noticed a smell but did not feel any wind coming out of him.</li>
    <li>Eating food that is made for ‘Ashoora’.</li>
    <li>Hijab in Islam is not due to sexual obsession.</li>
    <li>Will the person who intends to fast ‘Ashoora during the day be rewarded for his fasting?</li>
    <li>Recommendation to fast Taasoo’a’ with ‘Ashoora’.</li>
    <li>‘Aashoora’ in Islam and previous religions, and refutation of the Raafidi claim that it is an innovation introduced by the Umayyads.</li>
    <li>Her husband reviles Islam and does not pray, but if she gets divorced from him, she will be forced to work and take off her hijab.</li>
    <li>The virtue of fasting ‘Ashoora’.</li>
  </ul>
  <a class="abs btn" style="left:148px;top:793px">View All New Fatwas <svg viewBox="0 0 7 10"><path d="M1 1l4 4-4 4" stroke="#fff" stroke-width="2" fill="none"/></svg></a>

  <ul class="abs checks cats">
    <li>Basic Tenets of Faith.</li>
    <li>The Quraan and its Sciences.</li>
    <li>Hadeeth &amp; its Sciences.</li>
    <li>Rulings on Jihaad.</li>
    <li>Fiqh of the family.</li>
    <li>Islamic history and biography.</li>
    <li>Enjoining what is good and forbidding what is evil.</li>
    <li>Pedagogy education and upbringing.</li>
    <li>Psychological and Social Problems.</li>
    <li>Islamic politics.</li>
  </ul>
  <a class="abs btn" style="left:625px;top:793px">Read More <svg viewBox="0 0 7 10"><path d="M1 1l4 4-4 4" stroke="#fff" stroke-width="2" fill="none"/></svg></a>

  <div class="abs tabs">
    <div class="tab-on" style="width:110px">Counselling</div>
    <div style="width:133px">Jurisprudence of<br>Acts of Worship</div>
    <div style="width:142px">Jurisprudence of<br>Muslim Minorities</div>
    <div style="width:125px">Contemporary<br>Transactions</div>
    <div style="width:117px">Basic Tenets<br>of Faith</div>
    <div style="width:106px">The Muslim<br>Woman</div>
  </div>
  <ul class="abs checks counsel">
    <li>Her fiancé refuses to let her wear hijab.</li>
    <li>His wife torments his daughter from another wife, and he has a son from her, and he is confused as to how he should deal with her.</li>
    <li>A woman asking for a divorce from her husband who is addicted to drugs.</li>
    <li>He did the marriage contract with her and was intimate with her without intercourse in Ramadaan, and he had intercourse with her before announcing the marriage!</li>
  </ul>
  <a class="abs btn" style="left:149px;top:1004px">Read More <svg viewBox="0 0 7 10"><path d="M1 1l4 4-4 4" stroke="#fff" stroke-width="2" fill="none"/></svg></a>
</main>

<footer>
  <div class="abs footer"></div>
  <div class="abs fcol" style="left:135px"><h4>Information</h4><p>» Home<br>» About us<br>» Introduction of Islam<br>» Contact Us</p></div>
  <div class="abs fsep" style="left:277px"></div>
  <div class="abs fcol" style="left:325px"><h4>Usefull Links</h4><p>» Catagories<br>» New Fatwas<br>» Article &amp; Books<br>» Send a Questions</p></div>
  <div class="abs fsep" style="left:461px"></div>
  <div class="abs fbig" style="left:518px;top:1074px">Follow us on</div>
  <div class="abs soc" style="left:519px;top:1102px;background:#3b5a9a"></div>
  <div class="abs soc" style="left:548px;top:1102px;background:#1da1e2"></div>
  <div class="abs soc" style="left:578px;top:1102px;background:#f39a1e"></div>
  <div class="abs fsep" style="left:657px"></div>
  <div class="abs fbig" style="left:708px;top:1074px">Signup News Letter</div>
  <div class="abs email">Enter your Email ...</div>
  <div class="abs signup">Signup</div>
  <div class="abs copy">Copyright © <b>Velmor Hub</b> &nbsp;2013 &nbsp;44.78. All Right Reserved.</div>
</footer>

</body>
</html>
```